Vellora Premium Gel Top Coat and Base Coat Promotion

We need an eye catching flyer sized 8.5"x11" to promote a new product to our customers. We are promoting our own brand of gel nail polish top coat and base coat to nail salon customers in the Northeast USA. Basic layout of flyer is attached, as well as our company logo and product pictures. Attached picture of small nail polish bottles is a sample picture only - it needs to be changed or altered to show 16 bottles (2 rows of 8 bottles).

Target Market(s)

retail nail salon owners in the Northeast USA

Industry/Entity Type

Nail

Font styles to use
Sans Serif
Other font styles liked:
• designers' choices

Requirements
Must have
• Basic layout with all the text, logo and pictures attached
• New or altered picture of 16 nail polish bottles: 2 rows of 8 each
Nice to have
• Different fonts and or colors, banners, borders, etc.

```html
<!DOCTYPE html>
<html lang="en">
<head>
<meta charset="utf-8">
<title>Vellora Premium Gel Top Coat and Base Coat Promotion</title>
<link href="https://fonts.googleapis.com/css2?family=Montserrat:wght@500;600;700;800&display=swap" rel="stylesheet">
<style>
:root{
  --page-bg:#646b7c;
  --brand-blue:#0b62ad;
  --brand-blue-dark:#08508f;
  --ink:#1d1d1f;
  --white:#ffffff;
  --panel-light:#f2f2f2;
  --panel-mid:#d6d6d6;
  --divider:#9a9a9a;
}
*{margin:0;padding:0;box-sizing:border-box}
html,body{width:1200px;height:1200px;overflow:hidden}
body{background:var(--page-bg);font-family:'Montserrat',sans-serif;color:var(--ink);position:relative}
.flyer{position:absolute;left:136px;top:0;width:926px;height:1200px;overflow:hidden}
.abs{position:absolute}

/* hero */
.hero{left:0;top:0;width:926px;height:465px;background:linear-gradient(90deg,#101010 0%,#3a3a3a 35%,#8a8d92 65%,#b9bcc0 100%)}
.brand-mark{left:68px;top:120px;display:flex;align-items:center;gap:10px}
.brand-dot{width:26px;height:26px;border-radius:50%;background:var(--brand-blue)}
.brand-name{font-size:30px;font-weight:800;color:var(--white);line-height:1}
.brand-tag{left:104px;top:156px;font-size:11px;font-weight:600;color:var(--white);letter-spacing:.3px}
.headline{left:67px;top:302px;color:var(--white);line-height:1}
.headline .l1{font-size:35px;font-weight:600;letter-spacing:1px}
.headline .l2{font-size:35px;font-weight:700;color:var(--brand-blue);margin-top:3px;letter-spacing:.5px}
.headline .l3{font-size:50px;font-weight:800;margin-top:4px;letter-spacing:1px}

/* feature band */
.features{left:0;top:465px;width:926px;height:162px;background:linear-gradient(180deg,var(--brand-blue) 0%,var(--brand-blue) 80%,var(--brand-blue-dark) 100%)}
.feature{position:absolute;top:28px;width:160px;margin-left:-80px;text-align:center;color:var(--white)}
.feature svg{display:block;margin:0 auto}
.feature .rule{width:28px;height:3px;background:var(--white);margin:12px auto 0}
.feature .label{font-size:14px;font-weight:700;margin-top:19px;letter-spacing:.3px}

/* offer panel */
.offer{left:0;top:627px;width:926px;height:432px;background:linear-gradient(180deg,#e6e6e6 0%,var(--panel-light) 40%,#ffffff 60%,var(--panel-mid) 100%)}
.refill-title{left:67px;top:37px;font-size:20px;font-weight:700;letter-spacing:1.5px}
.refill-price{left:130px;top:62px;font-size:22px;font-weight:700;letter-spacing:.5px}
.refill-price b{color:var(--brand-blue);font-size:27px;font-weight:700}
.refill-photo{left:67px;top:118px;width:252px;height:292px;border-radius:6px;background:radial-gradient(ellipse at 50% 55%,#5a3312 0%,#3a220c 55%,#e4e4e4 80%)}
.vrule{left:383px;top:38px;width:3px;height:360px;background:var(--divider)}
.hrule{left:386px;top:168px;width:473px;height:3px;background:var(--divider)}
.guarantee{left:456px;top:37px}
.guarantee h2{font-size:20px;font-weight:700;color:var(--brand-blue);letter-spacing:.5px}
.guarantee p{font-size:16.5px;font-weight:600;margin-top:9px}
.guarantee p+p{margin-top:8px}
.cmp-label{font-size:17px;font-weight:700}
.cmp-price{font-size:28px;font-weight:700;color:var(--brand-blue);line-height:1.1}
.cmp-price small{font-size:17px;color:var(--ink)}
.one{left:456px;top:195px}
.sixteen{left:597px;top:195px}
.equals{font-size:30px;font-weight:800}
.eq1{left:546px;top:205px}
.eq2{left:546px;top:318px}
.small-photo{left:456px;top:262px;width:56px;height:135px;border-radius:5px;background:linear-gradient(180deg,#2a1a0a 0%,#5a3312 40%,#3a220c 100%)}
.bottles-photo{left:597px;top:258px;width:262px;height:140px;border-radius:5px;background:linear-gradient(180deg,#cfd2d6 0%,#eef0f2 50%,#c8cbcf 100%)}

/* footer */
.footer{left:0;top:1059px;width:926px;height:141px;background:linear-gradient(180deg,var(--brand-blue) 0%,var(--brand-blue) 70%,var(--brand-blue-dark) 100%);color:var(--white)}
.contact{left:67px;top:26px;font-size:15px;font-weight:500;line-height:27.5px}
.contact b{font-weight:700}
.contact .sep{margin:0 8px}
.company-box{left:598px;top:31px;width:261px;height:67px;border:3px solid var(--white);display:flex;align-items:center;justify-content:center;font-size:26px;font-weight:600;letter-spacing:.5px}
</style>
</head>
<body>
<main class="flyer">

  <section class="abs hero" role="img" aria-label="Photo of a young woman with long brown hair in profile, touching her chin, against a grey wall">
  </section>
  <div class="abs brand-mark"><span class="brand-dot"></span><span class="brand-name">Tidecrest</span></div>
  <div class="abs brand-tag">Wholesale Nail Supplies</div>
  <h1 class="abs headline">
    <div class="l1">THE BEST GEL</div>
    <div class="l2">TOP COAT/BASE COAT</div>
    <div class="l3">IN THE MARKET</div>
  </h1>

  <section class="abs features">
    <div class="feature" style="left:118px">
      <svg width="50" height="50" viewBox="0 0 50 50" fill="none" stroke="#fff" stroke-width="2"><circle cx="25" cy="25" r="23"/><rect x="20" y="20" width="10" height="15" rx="2" fill="#fff"/><rect x="22" y="13" width="6" height="7" fill="#fff"/><path d="M13 16l2 0M14 15l0 2M36 14l2 0M37 13l0 2M35 32l2 0M36 31l0 2"/></svg>
      <div class="rule"></div><div class="label">SUPER SHINY</div>
    </div>
    <div class="feature" style="left:289px">
      <svg width="50" height="50" viewBox="0 0 50 50" fill="none" stroke="#fff" stroke-width="2"><circle cx="25" cy="25" r="23"/><rect x="14" y="17" width="22" height="10" fill="#fff"/><rect x="21" y="27" width="9" height="10" rx="2"/><path d="M12 38L38 12"/></svg>
      <div class="rule"></div><div class="label">NO WIPE</div>
    </div>
    <div class="feature" style="left:462px">
      <svg width="50" height="50" viewBox="0 0 50 50" fill="none" stroke="#fff" stroke-width="2"><circle cx="25" cy="25" r="23"/><path d="M20 36V18l6-6 4 4-4 6v14z" fill="#fff"/><path d="M12 38L38 12"/></svg>
      <div class="rule"></div><div class="label">NO CHIP</div>
    </div>
    <div class="feature" style="left:630px">
      <svg width="50" height="50" viewBox="0 0 50 50" fill="none" stroke="#fff" stroke-width="2"><circle cx="25" cy="25" r="23"/><path d="M20 36V20a5 5 0 0110 0v16z" fill="#f3d23a" stroke="none"/><path d="M12 38L38 12"/></svg>
      <div class="rule"></div><div class="label">NON YELLOWING</div>
    </div>
    <div class="feature" style="left:796px">
      <svg width="50" height="50" viewBox="0 0 50 50" fill="none" stroke="#fff" stroke-width="2"><circle cx="25" cy="25" r="23"/><path d="M18 36c-3-5 3-8 0-13s2-8 2-8M25 36c-3-5 3-8 0-13s2-8 2-8M32 36c-3-5 3-8 0-13s2-8 2-8"/><path d="M12 38L38 12"/></svg>
      <div class="rule"></div><div class="label">NO BAD SMELL</div>
    </div>
  </section>

  <section class="abs offer">
    <div class="abs refill-title">8 OZ. REFILL BOTTLE</div>
    <div class="abs refill-price"><b>$60</b>/EACH</div>
    <div class="abs refill-photo" role="img" aria-label="Two amber 8 oz Vellora Premium Gel bottles, one Top Coat and one Base Coat"></div>

    <div class="abs vrule"></div>
    <div class="abs guarantee">
      <h2>SATISFACTION GUARANTEED !!!!!</h2>
      <p>Test for 2 weeks for FREE !!!</p>
      <p>If you love it, You buy it</p>
      <p>If you don't love it, we pick up &amp; you pay $0</p>
    </div>
    <div class="abs hrule"></div>

    <div class="abs one"><div class="cmp-label">(1) 8 oz.</div><div class="cmp-price">$60</div></div>
    <div class="abs equals eq1">=</div>
    <div class="abs sixteen"><div class="cmp-label">(16) .5 oz.</div><div class="cmp-price">$3.75<small>/Each</small></div></div>
    <div class="abs small-photo" role="img" aria-label="One amber 8 oz Vellora Premium Gel Top Coat bottle"></div>
    <div class="abs equals eq2">=</div>
    <div class="abs bottles-photo" role="img" aria-label="Sixteen small clear nail polish bottles with black caps in two rows of eight"></div>
  </section>

  <footer class="abs footer">
    <div class="abs contact">
      <div>48 Harbor Ave. Salem, MA 01970</div>
      <div><b>Phone</b> &nbsp;000 555 0142<span class="sep">I</span><b>Fax</b> &nbsp;000 555 0142</div>
      <div><b>Email</b> &nbsp;orders@tidecrestnail.com<span class="sep">I</span><b>Website</b> &nbsp;www.tidecrestnail.com</div>
    </div>
    <div class="abs company-box">Tidecrest Co.</div>
  </footer>

</main>
</body>
</html>
```